Valtren Power Core Values Poster

We want to display our company core values around our business. we want a poster that lists them with some cool solar graphics attached. This is to inspire and motivate our employees, promote our company and continue to adhere to a high code of conduct.

kladsf al asa kajdlkj akdj afa sdlkdjalk a dj faklsdoejsd poj dfoperjeo aod sd oe e oeoee fr oeoeo oee oeoeoe eooeoeoe eoeoeoeododoeoo dd d od d o d dddo doododo do dodododo do do doododo dodo odododododo dododoododododododododood ododo dododo

Target Market(s)

Employees

Industry/Entity Type

Solar Energy

Font styles to use
Serif

Colors
3176b5

Requirements
Must have
• All of the listed content in core values document. Can be multiple posters
Nice to have
• inspirational pictures
Should not have
• N/A

```html
<!DOCTYPE html>
<html lang="en">
<head>
<meta charset="utf-8">
<title>Valtren Power — Mission, Vision, Core Values Posters</title>
<link href="https://fonts.googleapis.com/css2?family=Arvo:wght@400;700&family=Noto+Serif:wght@400;700&display=swap" rel="stylesheet">
<style>
  :root {
    --page-bg: #e7e7e7;
    --poster-bg: #ffffff;
    --poster-fade: #eeeeee;
    --ink: #1f2d55;
    --brand-blue: #3176b5;
    --mission: #6f8f0c;
    --mission-dark: #2f3f05;
    --vision: #c26a22;
    --vision-dark: #4a2a10;
    --values: #5a93a8;
    --values-dark: #1e3f52;
  }
  * { box-sizing: border-box; margin: 0; padding: 0; }
  html, body { width: 1200px; height: 864px; overflow: hidden; }
  body {
    background: var(--page-bg);
    font-family: "Noto Serif", Georgia, serif;
    color: var(--ink);
    position: relative;
  }
  .poster {
    position: absolute;
    top: 216px;
    width: 334px;
    height: 466px;
    background: linear-gradient(to bottom, var(--poster-bg) 55%, var(--poster-fade));
    box-shadow: 0 6px 16px rgba(0,0,0,0.18);
    overflow: hidden;
  }
  .poster--mission { left: 68px; }
  .poster--vision { left: 440px; }
  .poster--values { left: 812px; }
  .poster__art { position: absolute; top: 0; left: 0; width: 334px; height: 290px; display: block; }
  .poster__title {
    position: absolute;
    top: 326px;
    left: 0; right: 0;
    text-align: center;
    font-family: "Arvo", Georgia, serif;
    font-weight: 700;
    font-size: 35px;
    letter-spacing: -0.5px;
    line-height: 1;
  }
  .poster--mission .poster__title { color: var(--mission); }
  .poster--vision .poster__title { color: var(--vision); }
  .poster--values .poster__title { color: var(--values); }
  .poster__statement {
    position: absolute;
    top: 374px;
    left: 84px;
    right: 84px;
    font-size: 7.4px;
    line-height: 1.35;
    text-align: justify;
  }
  .poster--mission .poster__statement { left: 85px; right: 20px; top: 376px; }
  .poster--vision .poster__statement { left: 86px; right: 58px; top: 376px; }
  .values-list {
    position: absolute;
    top: 374px;
    left: 42px;
    right: 30px;
    display: flex;
    list-style: none;
  }
  .value {
    flex: 1;
    padding: 0 7px;
    border-left: 1px solid var(--ink);
  }
  .value:first-child { border-left: none; padding-left: 0; }
  .value__name { font-size: 8.6px; font-weight: 700; margin-bottom: 4px; }
  .value__text { font-size: 5.6px; line-height: 1.35; }
  .brand {
    position: absolute;
    top: 428px;
    left: 0; right: 0;
    text-align: center;
    font-family: "Arvo", Georgia, serif;
    font-weight: 700;
    font-size: 12px;
    color: var(--brand-blue);
  }
</style>
</head>
<body>

<section class="poster poster--mission">
  <svg class="poster__art" viewBox="0 0 334 290" role="img" aria-label="Photo of engineers in hard hats reviewing plans beside a solar farm at sunset, green tint">
    <defs>
      <linearGradient id="missionTone" x1="0" y1="0" x2="0" y2="1">
        <stop offset="0" stop-color="#7d9c12"/>
        <stop offset="0.6" stop-color="#5e7a0a"/>
        <stop offset="1" stop-color="#2b3a05"/>
      </linearGradient>
      <radialGradient id="missionSun" cx="0.5" cy="0.57" r="0.18">
        <stop offset="0" stop-color="#fff6c8"/>
        <stop offset="0.3" stop-color="#f0c040" stop-opacity="0.7"/>
        <stop offset="1" stop-color="#f0c040" stop-opacity="0"/>
      </radialGradient>
    </defs>
    <path d="M0 0H334V205C300 258 235 282 165 276C95 270 30 230 0 125Z" fill="url(#missionTone)"/>
    <path d="M0 0H334V205C300 258 235 282 165 276C95 270 30 230 0 125Z" fill="url(#missionSun)"/>
    <path d="M0 120C30 225 95 268 170 272C240 276 300 252 334 208" fill="none" stroke="#fff" stroke-width="6"/>
    <path d="M0 150C40 240 120 280 200 280C260 280 310 262 334 238" fill="none" stroke="var(--mission-dark)" stroke-width="7"/>
    <path d="M10 180C60 255 140 288 220 286C270 284 310 272 334 262" fill="none" stroke="#fff" stroke-width="3"/>
  </svg>
  <h2 class="poster__title">MISSION</h2>
  <p class="poster__statement">Provide our customers with the highest quality, renewable energy products and services to maximize their savings and give them the freedom to power anything, anywhere.</p>
  <div class="brand">Valtren Power</div>
</section>

<section class="poster poster--vision">
  <svg class="poster__art" viewBox="0 0 334 290" role="img" aria-label="Photo of a crew installing solar panels on a roof at sunset, orange tint">
    <defs>
      <linearGradient id="visionTone" x1="0" y1="0" x2="0" y2="1">
        <stop offset="0" stop-color="#d08a40"/>
        <stop offset="0.55" stop-color="#a85a1c"/>
        <stop offset="1" stop-color="#3e230c"/>
      </linearGradient>
      <radialGradient id="visionSun" cx="0.5" cy="0.32" r="0.16">
        <stop offset="0" stop-color="#fff4d0"/>
        <stop offset="0.3" stop-color="#f5b050" stop-opacity="0.7"/>
        <stop offset="1" stop-color="#f5b050" stop-opacity="0"/>
      </radialGradient>
    </defs>
    <path d="M0 0H334V205C300 258 235 282 165 276C95 270 30 230 0 125Z" fill="url(#visionTone)"/>
    <path d="M0 0H334V205C300 258 235 282 165 276C95 270 30 230 0 125Z" fill="url(#visionSun)"/>
    <path d="M0 120C30 225 95 268 170 272C240 276 300 252 334 208" fill="none" stroke="#fff" stroke-width="6"/>
    <path d="M0 150C40 240 120 280 200 280C260 280 310 262 334 238" fill="none" stroke="var(--vision-dark)" stroke-width="7"/>
    <path d="M10 180C60 255 140 288 220 286C270 284 310 272 334 262" fill="none" stroke="#fff" stroke-width="3"/>
  </svg>
  <h2 class="poster__title">VISION</h2>
  <p class="poster__statement">Continue to be a full service renewable energy company providing solar, battery storage, off-grid, service, and maintenance solutions.</p>
  <div class="brand">Valtren Power</div>
</section>

<section class="poster poster--values">
  <svg class="poster__art" viewBox="0 0 334 290" role="img" aria-label="Photo of a technician working on a rooftop solar array under a cloudy sky, blue tint">
    <defs>
      <linearGradient id="valuesTone" x1="0" y1="0" x2="0" y2="1">
        <stop offset="0" stop-color="#4f7f94"/>
        <stop offset="0.35" stop-color="#9fc3cf"/>
        <stop offset="0.55" stop-color="#5b8ea3"/>
        <stop offset="1" stop-color="#1b3547"/>
      </linearGradient>
      <radialGradient id="valuesSun" cx="0.45" cy="0.38" r="0.14">
        <stop offset="0" stop-color="#fff3c8"/>
        <stop offset="0.3" stop-color="#f2b34a" stop-opacity="0.7"/>
        <stop offset="1" stop-color="#f2b34a" stop-opacity="0"/>
      </radialGradient>
    </defs>
    <path d="M0 0H334V205C300 258 235 282 165 276C95 270 30 230 0 125Z" fill="url(#valuesTone)"/>
    <path d="M0 0H334V205C300 258 235 282 165 276C95 270 30 230 0 125Z" fill="url(#valuesSun)"/>
    <path d="M0 120C30 225 95 268 170 272C240 276 300 252 334 208" fill="none" stroke="#fff" stroke-width="6"/>
    <path d="M0 150C40 240 120 280 200 280C260 280 310 262 334 238" fill="none" stroke="var(--values-dark)" stroke-width="7"/>
    <path d="M10 180C60 255 140 288 220 286C270 284 310 272 334 262" fill="none" stroke="#fff" stroke-width="3"/>
  </svg>
  <h2 class="poster__title">CORE VALUES</h2>
  <ul class="values-list">
    <li class="value"><h3 class="value__name">Integrity</h3><p class="value__text">Do the right thing</p></li>
    <li class="value"><h3 class="value__name">Quality</h3><p class="value__text">Provide excellent components and construction that stand the test of time</p></li>
    <li class="value"><h3 class="value__name">Service</h3><p class="value__text">Meet the customers' needs today, tomorrow, and for life</p></li>
    <li class="value"><h3 class="value__name">Value</h3><p class="value__text">The most savings for the money.</p></li>
  </ul>
  <div class="brand">Valtren Power</div>
</section>

</body>
</html>
```